Business card design for global fintech startup

Veltrix is a modern payments platform for the global insurance industry, serving international health, life, and travel insurers, MGAs, brokers, and partners.

We need a professional, premium business card for use at insurance conferences and executive meetings. The goal is to create a card that feels trustworthy, modern, and high-quality, while still being distinctive and memorable in a stack of business cards.

Target audience:
Senior insurance executives (VP, C-suite).

Design goals:
Clear, professional, and credible
Modern but not trendy
Premium and well-structured
Easy to read and practical for networking

Brand direction:
Brand-first (company over individual)
Follow existing brand guidelines where possible
Clean layout, strong hierarchy, excellent readability

Must include:
Name
Title
Company name (Veltrix)
Logo
Email
Phone/Whatsapp
Website (www.withveltrix.example)
Tagline - Trust that moves money

Materials & finish:
Open to designer recommendations for premium look and feel.

Please avoid:
Flashy or trendy startup styles
Generic insurance icons or clichés
Cluttered layouts or hard-to-read text

Deliverables:
Front and back business card, print-ready files.

Target Market(s)

Global Insurance executives

Industry/Entity Type

Fintech, Insurtech, Insurance, Financial Services

Contact Information for Business Card

Name Title Company name (Veltrix) Logo Email Phone/Whatsapp Website (www.withveltrix.example) Tagline - Trust that moves money

Font styles to use
Other font styles liked:
• See brand guidelines

Requirements
Nice to have
• something that stands out/makes us more memorable while still remaining professional
Should not have
• Please avoid: Flashy or trendy startup styles Generic insurance icons or clichés Cluttered layouts or hard-to-read text

```html
<!DOCTYPE html>
<html lang="en">
<head>
<meta charset="utf-8">
<title>Veltrix Business Cards</title>
<link href="https://fonts.googleapis.com/css2?family=Ubuntu:wght@400;500;700&display=swap" rel="stylesheet">
<style>
  :root {
    --bg: #e8e5e1;
    --ink: #1c1c1e;
    --white: #ffffff;
    --black: #000000;
    --purple: #5b3f9a;
    --cyan: #3cc3ea;
    --orange: #f07d22;
    --rule: #cfcfcf;
    --sky: #a6e3f4;
    --peach: #f9e6d6;
  }
  * { margin: 0; padding: 0; box-sizing: border-box; }
  html, body { width: 1200px; height: 995px; overflow: hidden; }
  body {
    background: var(--bg);
    font-family: "Ubuntu", sans-serif;
    color: var(--ink);
    position: relative;
  }
  .card {
    position: absolute;
    width: 520px;
    height: 300px;
    box-shadow: 0 8px 24px rgba(0,0,0,0.18);
    overflow: hidden;
  }

  /* Front card */
  .card-front { left: 60px; top: 150px; background: var(--white); }
  .brand-lockup {
    position: absolute; left: 90px; top: 48px;
    display: flex; align-items: center; gap: 22px;
  }
  .brand-dot { width: 46px; height: 46px; border-radius: 50%; background: var(--orange); }
  .brand-name {
    font-weight: 500; font-size: 56px; letter-spacing: 6px;
    color: var(--ink); text-transform: uppercase;
  }
  .holder {
    position: absolute; left: 0; right: 0; top: 148px; text-align: center;
  }
  .holder-name { font-weight: 700; font-size: 21px; color: var(--purple); }
  .holder-title {
    font-weight: 700; font-size: 10px; color: var(--cyan);
    letter-spacing: 0.5px; vertical-align: 7px;
  }
  .rule { height: 1px; background: var(--rule); width: 90px; margin: 8px auto 0; }
  .contacts {
    position: absolute; left: 0; right: 0; top: 196px;
    display: flex; justify-content: center; gap: 22px;
    font-size: 12px; color: var(--ink);
  }
  .contact { display: flex; align-items: center; gap: 5px; }
  .contact svg { width: 14px; height: 14px; flex: none; }
  .front-rule { position: absolute; left: 215px; top: 226px; width: 90px; height: 1px; background: var(--rule); }
  .front-tagline {
    position: absolute; left: 0; right: 0; top: 240px; text-align: center;
    font-weight: 500; font-size: 19px; letter-spacing: 0.5px; text-transform: uppercase;
  }

  /* Back card, dark */
  .card-back-dark { left: 620px; top: 150px; background: var(--black); color: var(--white); }
  .dark-brand {
    position: absolute; left: 46px; top: 120px;
    display: flex; align-items: center; gap: 14px;
  }
  .dark-brand .brand-dot { width: 30px; height: 30px; }
  .dark-brand .brand-word { font-weight: 500; font-size: 34px; color: var(--white); }
  .dark-tagline {
    position: absolute; left: 270px; top: 86px;
    font-weight: 500; font-size: 30px; line-height: 1.15;
  }
  .dark-rule { position: absolute; left: 270px; top: 166px; width: 210px; height: 1px; background: #555; }
  .dark-url {
    position: absolute; left: 270px; top: 180px;
    font-size: 14px; letter-spacing: 2px;
  }

  /* Back card, gradient */
  .card-back-light {
    left: 340px; top: 545px;
    background: linear-gradient(90deg, var(--sky) 0%, #e4f4f6 45%, var(--peach) 100%);
  }
  .light-brand {
    position: absolute; left: 0; right: 0; top: 56px;
    display: flex; justify-content: center; align-items: center; gap: 10px;
  }
  .light-brand .brand-dot { width: 22px; height: 22px; }
  .light-brand .brand-word { font-weight: 500; font-size: 24px; color: var(--ink); }
  .light-tagline {
    position: absolute; left: 0; right: 0; top: 118px; text-align: center;
    font-weight: 500; font-size: 40px; color: var(--ink);
  }
  .light-url {
    position: absolute; left: 0; right: 0; top: 208px; text-align: center;
    font-weight: 500; font-size: 17px; letter-spacing: 2px; color: var(--ink);
  }
  .light-url .url-name { color: var(--purple); }
</style>
</head>
<body>

  <section class="card card-front" aria-label="Business card front">
    <div class="brand-lockup">
      <span class="brand-dot"></span>
      <span class="brand-name">Veltrix</span>
    </div>
    <div class="holder">
      <span class="holder-name">Daniel Mercer,</span>
      <span class="holder-title">OWNER</span>
      <div class="rule"></div>
    </div>
    <div class="contacts">
      <span class="contact">
        <svg viewBox="0 0 16 16"><circle cx="8" cy="8" r="7" fill="none" stroke="var(--orange)" stroke-width="1.6"/><path d="M5.5 4.5l1.5 0 .6 2-1 .8a5 5 0 0 0 2.2 2.2l.8-1 2 .6 0 1.5c-3.5.3-6.4-2.6-6.1-6.1z" fill="var(--orange)"/></svg>
        555.010.2468
      </span>
      <span class="contact">
        <svg viewBox="0 0 16 16"><path d="M3 2.5h3l1 3-1.6 1.2a7 7 0 0 0 3.9 3.9L10.5 9l3 1v3c-6 .5-11-4.5-10.5-10.5z" fill="var(--orange)"/></svg>
        555.010.1357
      </span>
      <span class="contact">
        <svg viewBox="0 0 16 16"><rect x="1.5" y="3.5" width="13" height="9" rx="1.5" fill="var(--orange)"/><path d="M2 4.5l6 4.5 6-4.5" fill="none" stroke="var(--white)" stroke-width="1.3"/></svg>
        info@withveltrix.example
      </span>
    </div>
    <div class="front-rule"></div>
    <p class="front-tagline">Trust That Moves Money</p>
  </section>

  <section class="card card-back-dark" aria-label="Business card back, dark">
    <div class="dark-brand">
      <span class="brand-dot"></span>
      <span class="brand-word">Veltrix</span>
    </div>
    <p class="dark-tagline">Trust That<br>Moves Money</p>
    <div class="dark-rule"></div>
    <p class="dark-url">www.withveltrix.example</p>
  </section>

  <section class="card card-back-light" aria-label="Business card back, light">
    <div class="light-brand">
      <span class="brand-dot"></span>
      <span class="brand-word">Veltrix</span>
    </div>
    <p class="light-tagline">Trust That Moves Money</p>
    <p class="light-url">www.<span class="url-name">withveltrix</span>.example</p>
  </section>

</body>
</html>
```